vintage travel patch design for luggage brand

We are a travel and lifestyle design brand based in Costa Rica, designing travel patches for our luggage pieces. We will reinterpret vintage destination tags with our logo. At the moment we need individual images of each luggage tags that will then be manufactured into patches for our luggage. Using existing ones as a template I would like to recreate our own version where the destination airport can be changed as needed.

Target Market(s)

it may be helpful to see our website. www.quillbramblegoods.com for an idea of product

Industry/Entity Type

Fashion

Requirements
Must have
• The attached files are templates to use. We would like to create our own, but not to different in design than what is shown as we want them to identifiable and instantly recognizable as airport codes and tags. The idea is to be able to change the airport code as needed on a few templates.
• For this reason it could be an ongoing project

```html
<!DOCTYPE html>
<html lang="en">
<head>
<meta charset="utf-8">
<title>Quillbramble Goods – Luggage Tag</title>
<link rel="stylesheet" href="https://fonts.googleapis.com/css2?family=Arimo:wght@400;700&family=Poiret+One&display=swap">
<style>
  :root {
    --paper: #ffffff;
    --outline: #b9b9b9;
    --rule: #9c9c9c;
    --brand-grey: #9a9a9a;
    --label-navy: #231b8c;
    --stamp-red: #e11d15;
    --stamp-ink: #111111;
    --grommet-ring: #f3c48c;
    --grommet-edge: #c9c9c9;
  }
  html, body {
    margin: 0;
    padding: 0;
    overflow: hidden;
    background: var(--paper);
  }
  .tag {
    position: relative;
    width: 1200px;
    height: 2396px;
    overflow: hidden;
    background: var(--paper);
  }
  .tag-shape {
    position: absolute;
    inset: 0;
  }
  .brand-name {
    position: absolute;
    left: 40px;
    width: 1120px;
    top: 770px;
    margin: 0;
    font-family: "Poiret One", sans-serif;
    font-weight: 400;
    color: var(--brand-grey);
    text-transform: uppercase;
    line-height: 1;
    text-align: center;
  }
  .brand-name .line {
    display: block;
    font-size: 132px;
    letter-spacing: 6px;
  }
  .brand-name .line + .line {
    margin-top: 18px;
  }
  .field-label {
    position: absolute;
    left: 64px;
    margin: 0;
    font-family: "Arimo", Arial, sans-serif;
    font-size: 56px;
    font-weight: 400;
    color: var(--label-navy);
    line-height: 1;
  }
  .field-name { top: 1166px; }
  .field-address { top: 1294px; }
  .field-phone { top: 1450px; }
  .stamp {
    position: absolute;
    width: 240px;
    height: 120px;
  }
  .stamp svg {
    position: absolute;
    inset: 0;
  }
  .stamp-word {
    position: absolute;
    left: -20px;
    right: -20px;
    top: 18px;
    text-align: center;
    font-family: "Arimo", Arial, sans-serif;
    font-weight: 700;
    font-size: 60px;
    color: var(--stamp-ink);
    line-height: 1;
  }
</style>
</head>
<body>
<main class="tag">
  <svg class="tag-shape" width="1200" height="2396" viewBox="0 0 1200 2396" aria-hidden="true">
    <path d="M3 2393 V480 A477 477 0 0 1 480 3 H720 A477 477 0 0 1 1197 480 V2393 Z"
          fill="var(--paper)" stroke="var(--outline)" stroke-width="4"/>
    <circle cx="600" cy="148" r="72" fill="var(--grommet-ring)"/>
    <circle cx="600" cy="148" r="42" fill="var(--paper)" stroke="var(--grommet-edge)" stroke-width="6"/>
    <g stroke="var(--rule)" stroke-width="3">
      <line x1="3" y1="1152" x2="1197" y2="1152"/>
      <line x1="3" y1="1264" x2="1197" y2="1264"/>
      <line x1="3" y1="1434" x2="1197" y2="1434"/>
      <line x1="3" y1="1520" x2="1197" y2="1520"/>
    </g>
  </svg>

  <h1 class="brand-name"><span class="line">Quillbramble</span><span class="line">Goods</span></h1>

  <p class="field-label field-name">Name</p>
  <p class="field-label field-address">Address</p>
  <p class="field-label field-phone">Phone</p>

  <div class="stamp" style="left:144px; top:1534px;">
    <svg viewBox="0 0 240 120" width="240" height="120" aria-hidden="true">
      <ellipse cx="120" cy="60" rx="118" ry="56" fill="var(--stamp-red)"/>
      <polygon points="74,62 166,62 120,114" fill="var(--paper)"/>
    </svg>
    <span class="stamp-word">Flight</span>
  </div>
  <div class="stamp" style="left:810px; top:1534px;">
    <svg viewBox="0 0 240 120" width="240" height="120" aria-hidden="true">
      <ellipse cx="120" cy="60" rx="118" ry="56" fill="var(--stamp-red)"/>
      <polygon points="74,62 166,62 120,114" fill="var(--paper)"/>
    </svg>
    <span class="stamp-word">Transfer</span>
  </div>

  <div class="stamp" style="left:144px; top:1800px;">
    <svg viewBox="0 0 240 120" width="240" height="120" aria-hidden="true">
      <ellipse cx="120" cy="60" rx="118" ry="56" fill="var(--stamp-red)"/>
      <polygon points="74,62 166,62 120,114" fill="var(--paper)"/>
    </svg>
    <span class="stamp-word">Flight</span>
  </div>
  <div class="stamp" style="left:810px; top:1800px;">
    <svg viewBox="0 0 240 120" width="240" height="120" aria-hidden="true">
      <ellipse cx="120" cy="60" rx="118" ry="56" fill="var(--stamp-red)"/>
      <polygon points="74,62 166,62 120,114" fill="var(--paper)"/>
    </svg>
    <span class="stamp-word">Transfer</span>
  </div>

  <div class="stamp" style="left:144px; top:2064px;">
    <svg viewBox="0 0 240 120" width="240" height="120" aria-hidden="true">
      <ellipse cx="120" cy="60" rx="118" ry="56" fill="var(--stamp-red)"/>
      <polygon points="74,62 166,62 120,114" fill="var(--paper)"/>
    </svg>
    <span class="stamp-word">Flight</span>
  </div>
  <div class="stamp" style="left:810px; top:2064px;">
    <svg viewBox="0 0 240 120" width="240" height="120" aria-hidden="true">
      <ellipse cx="120" cy="60" rx="118" ry="56" fill="var(--stamp-red)"/>
      <polygon points="74,62 166,62 120,114" fill="var(--paper)"/>
    </svg>
    <span class="stamp-word">Transfer</span>
  </div>
</main>
</body>
</html>
```